Coffee roasting needs homepage with web shop

small roasting (no cafe!) needs a simple website with a web shop. We sell coffee to dealers and end customers. The shop should be for end consumers as well as for B2B customers. A login should be available. The design should be modern and at the same time classic with subtle (dark) colors. We need the tabs "Coffee, Shop, Contact, Coffee, Coffee, Login, About Us, Imprint, Privacy" Logo nr 1 should be used from attached file

Target Market(s)

B2B

Number of Pages Required

5+ page

Font styles to use
Sans Serif

Colors

Designer to choose only greyscale colors for use in the design.

Requirements
Must have
• Webshop

```html
<!DOCTYPE html>
<html lang="en">
<head>
<meta charset="utf-8">
<title>Brennwerk – Coffee Roasting</title>
<link href="https://fonts.googleapis.com/css2?family=Raleway:wght@300;400;500;700&family=Roboto:wght@400;500&family=Playfair+Display:wght@700&family=Tinos&display=swap" rel="stylesheet">
<style>
:root{
  --bg-dark:#1c1c1c;
  --bg-darker:#111111;
  --bg-footer-bar:#151515;
  --white:#ffffff;
  --text-soft:#dcdcdc;
  --muted:#8a8a8a;
  --rose:#b89a97;
  --nav-band:rgba(60,60,60,.55);
  --photo-brown-1:#2a1a12;
  --photo-brown-2:#6b4a33;
  --photo-brown-3:#a17a55;
  --photo-grey-1:#2b2b2b;
  --photo-grey-2:#7a7a7a;
}
*{margin:0;padding:0;box-sizing:border-box}
html,body{width:680px;height:1200px;overflow:hidden;background:var(--bg-dark)}
body{position:relative;font-family:"Roboto",Arial,sans-serif;color:var(--white)}
.abs{position:absolute}

/* Hero */
.hero{left:0;top:0;width:680px;height:315px;
  background:linear-gradient(180deg,var(--photo-brown-1) 0%,#3d2a1e 35%,var(--photo-brown-2) 60%,#4a3020 80%,var(--photo-brown-3) 100%)}
.hero-cup{left:360px;top:80px;width:280px;height:150px;border-radius:40% 40% 50% 50%;
  background:radial-gradient(ellipse at 50% 40%,#f1eeea 0%,#d8d2cc 45%,rgba(200,190,180,0) 72%)}
.nav-band{left:0;top:36px;width:680px;height:27px;background:var(--nav-band)}
.nav{top:44px;font-family:"Tinos",serif;font-size:8px;letter-spacing:.4px;color:var(--white);display:flex;gap:10px}
.nav .sep{color:var(--text-soft)}
.nav.main{left:329px}
.nav.account{left:546px;color:var(--text-soft)}
.brand-mark{left:51px;top:12px;width:74px;height:74px;border:1.5px solid var(--white);border-radius:50%;
  display:flex;align-items:center;justify-content:center;font-family:"Raleway",sans-serif;font-weight:500;font-size:12px;color:var(--white)}
.slide-arrow{width:22px;height:22px}
.welcome-band{left:0;top:278px;width:680px;height:37px;background:rgba(40,30,25,.35)}
.welcome{left:0;top:283px;width:680px;text-align:center;font-family:"Raleway",sans-serif;font-weight:300;font-size:22px}
.welcome b{font-weight:700}

/* Products */
.products{left:0;top:315px;width:680px;height:335px;background:var(--bg-dark)}
.eyebrow{left:0;top:346px;width:680px;text-align:center;font-family:"Playfair Display",serif;font-weight:700;font-size:11px;color:var(--rose)}
.section-title{left:0;top:361px;width:680px;text-align:center;font-family:"Raleway",sans-serif;font-weight:300;font-size:25px}
.product{top:416px;width:148px;text-align:center}
.product-photo{width:148px;height:90px}
.photo-a{background:linear-gradient(135deg,#d9c7ae 0%,#8a4a22 40%,#5a2c14 70%,#3a1c0e 100%)}
.photo-b{background:linear-gradient(120deg,#e8e2dc 0%,#b9a89a 30%,#4a2e1e 60%,#2a1a10 100%)}
.product-name{margin-top:11px;font-family:"Raleway",sans-serif;font-size:11px}
.product-price{margin-top:3px;font-family:"Raleway",sans-serif;font-weight:700;font-size:10px;color:var(--text-soft)}
.btn-outline{display:inline-block;border:1px solid var(--white);font-size:7.5px;color:var(--white);text-align:center;line-height:17px}
.product .btn-outline{margin-top:8px;width:67px;height:19px}

/* About */
.about{left:0;top:650px;width:680px;height:199px;background:var(--bg-darker)}
.who{left:100px;top:710px;width:73px;text-align:right;font-family:"Raleway",sans-serif;font-weight:300;font-size:21px;line-height:27px;letter-spacing:.5px}
.quote-mark{font-family:"Playfair Display",serif;font-weight:700;font-size:56px;line-height:1;color:#4a4a4a}
.about-text{left:253px;top:709px;width:303px;font-size:7.5px;line-height:12px;text-align:justify;color:var(--text-soft)}
.about-text p+p{margin-top:12px}
.about .btn-outline,.about-btn{left:253px;top:791px;width:67px;height:19px}

/* Business */
.business{left:0;top:849px;width:680px;height:242px;
  background:linear-gradient(100deg,#5c5c5c 0%,var(--photo-grey-2) 30%,#4a4a4a 60%,var(--photo-grey-1) 100%)}
.business-title{left:0;top:937px;width:680px;text-align:center;font-family:"Raleway",sans-serif;font-weight:300;font-size:25px}
.btn-solid{left:296px;top:975px;width:89px;height:22px;background:var(--white);color:#222;
  font-family:"Raleway",sans-serif;font-size:10px;letter-spacing:.5px;text-align:center;line-height:22px}

/* Footer */
.footer{left:0;top:1091px;width:680px;height:88px;background:var(--bg-dark)}
.contact-line{left:101px;display:flex;align-items:center;gap:5px;font-size:7.5px}
.contact-line svg{width:8px;height:8px}
.footer-mark{left:313px;top:1108px;width:55px;height:55px;border:1.5px solid var(--white);border-radius:50%;
  display:flex;align-items:center;justify-content:center;font-family:"Raleway",sans-serif;font-weight:500;font-size:9px}
.legal{right:101px;text-align:right;font-size:7.5px}
.social{top:1146px;width:12px;height:12px;border:1px solid var(--text-soft);border-radius:50%}
.copyright{left:0;top:1179px;width:680px;height:21px;background:var(--bg-footer-bar);
  text-align:center;font-size:6.5px;line-height:21px;letter-spacing:.3px;color:var(--text-soft)}
</style>
</head>
<body>

<header>
  <div class="abs hero" role="img" aria-label="Photo of a white coffee cup on a saucer with roasted coffee beans on burlap"></div>
  <div class="abs hero-cup" aria-hidden="true"></div>
  <div class="abs nav-band"></div>
  <div class="abs brand-mark">Brennwerk</div>
  <nav class="abs nav main"><span>COFFEE</span><span class="sep">/</span><span>SHOP</span><span class="sep">/</span><span>CONTACT</span><span class="sep">/</span><span>ABOUT</span></nav>
  <nav class="abs nav account"><span>SIGN UP</span><span class="sep">/</span><span>LOG IN</span></nav>
  <svg class="abs slide-arrow" style="left:10px;top:162px" viewBox="0 0 22 22"><circle cx="11" cy="11" r="10" fill="none" stroke="#fff" stroke-width="1"/><path d="M13 6 L8 11 L13 16" fill="none" stroke="#fff" stroke-width="1"/></svg>
  <svg class="abs slide-arrow" style="left:647px;top:162px" viewBox="0 0 22 22"><circle cx="11" cy="11" r="10" fill="none" stroke="#fff" stroke-width="1"/><path d="M9 6 L14 11 L9 16" fill="none" stroke="#fff" stroke-width="1"/></svg>
  <div class="abs welcome-band"></div>
  <h1 class="abs welcome" style="font-weight:300">Welcome to the <b>Brennwerk</b></h1>
</header>

<section>
  <div class="abs products"></div>
  <div class="abs eyebrow">Quality Roasted</div>
  <h2 class="abs section-title">PRODUCTS</h2>
  <svg class="abs" style="left:60px;top:455px;width:14px;height:14px" viewBox="0 0 14 14"><circle cx="7" cy="7" r="6.2" fill="none" stroke="#ccc" stroke-width=".8"/><path d="M8 4 L5 7 L8 10" fill="none" stroke="#ccc" stroke-width=".8"/></svg>
  <svg class="abs" style="left:601px;top:455px;width:14px;height:14px" viewBox="0 0 14 14"><circle cx="7" cy="7" r="6.2" fill="none" stroke="#ccc" stroke-width=".8"/><path d="M6 4 L9 7 L6 10" fill="none" stroke="#ccc" stroke-width=".8"/></svg>
  <div class="abs product" style="left:101px">
    <div class="product-photo photo-a" role="img" aria-label="Product photo of roasted coffee beans spilling from a cup"></div>
    <div class="product-name">Product Name</div><div class="product-price">€120</div>
    <span class="btn-outline">View More</span>
  </div>
  <div class="abs product" style="left:266px">
    <div class="product-photo photo-b" role="img" aria-label="Product photo of a coffee cup beside a burlap sack of beans"></div>
    <div class="product-name">Product Name</div><div class="product-price">€120</div>
    <span class="btn-outline">View More</span>
  </div>
  <div class="abs product" style="left:431px">
    <div class="product-photo photo-a" role="img" aria-label="Product photo of roasted coffee beans spilling from a cup"></div>
    <div class="product-name">Product Name</div><div class="product-price">€120</div>
    <span class="btn-outline">View More</span>
  </div>
</section>

<section>
  <div class="abs about"></div>
  <h2 class="abs who" style="font-weight:300">WHO<br>WE<br>ARE</h2>
  <div class="abs quote-mark" style="left:231px;top:668px">&ldquo;</div>
  <div class="abs about-text">
    <p>Lorem Ipsum is simply dummy text of the printing and typesetting industry. Lorem Ipsum has been the industry's standard dummy text ever since the 1500s, when an unknown printer took a galley of type and scrambled it to make a type specimen book.</p>
    <p>It has survived not only five centuries, but also the leap into electronic typesetting, remaining essentially unchanged.</p>
  </div>
  <span class="abs btn-outline about-btn">Know More</span>
  <div class="abs quote-mark" style="left:524px;top:792px">&rdquo;</div>
</section>

<section>
  <div class="abs business" role="img" aria-label="Greyscale photo of a latte cup and an open burlap sack of coffee beans"></div>
  <h2 class="abs business-title" style="font-weight:300">FOR BUSINESS</h2>
  <span class="abs btn-solid">CONTACT US</span>
</section>

<footer>
  <div class="abs footer"></div>
  <div class="abs contact-line" style="top:1118px">
    <svg viewBox="0 0 8 8"><path d="M4 7.6 C2 5 1.2 4 1.2 2.9 A2.8 2.8 0 0 1 6.8 2.9 C6.8 4 6 5 4 7.6Z" fill="none" stroke="#ccc" stroke-width=".8"/><circle cx="4" cy="3" r="1" fill="none" stroke="#ccc" stroke-width=".7"/></svg>
    <span>8000 Mühleweg, Talstadt</span></div>
  <div class="abs contact-line" style="top:1132px">
    <svg viewBox="0 0 8 8"><rect x=".8" y="1.8" width="6.4" height="4.6" fill="none" stroke="#ccc" stroke-width=".7"/><path d="M.8 1.8 L4 4.5 L7.2 1.8" fill="none" stroke="#ccc" stroke-width=".7"/></svg>
    <span>hallo@brennwerk.example</span></div>
  <div class="abs contact-line" style="top:1146px">
    <svg viewBox="0 0 8 8"><path d="M1.5 1 L3 1 L3.6 2.8 L2.7 3.5 C3.2 4.6 3.6 5 4.6 5.4 L5.3 4.5 L7 5.1 L7 6.6 C4 7 1 4 1.5 1Z" fill="#ccc"/></svg>
    <span>+41 (0)00 000 0000</span></div>
  <div class="abs footer-mark">Brennwerk</div>
  <div class="abs legal" style="top:1116px">Imprint</div>
  <div class="abs legal" style="top:1130px">Privacy Policy</div>
  <div class="abs social" style="left:535px"></div>
  <div class="abs social" style="left:551px"></div>
  <div class="abs social" style="left:567px"></div>
  <div class="abs copyright">© COPYRIGHT 2019 | ALL RIGHTS RESERVED.</div>
</footer>

</body>
</html>
```